Vantage Forge needs a powerpoint design

We need a powerpoint design for an Information Technology based in Fairfax call "Vantage Forge". We are Information Technology solutions provider for the Federal Government. We develop Kestrel, Mobile and Cloud based solutions. We support the Healthcare and Financial sectors of the Government. We would like to see designs that use the colors of our logo. We've attached a copy of our logo. The final design should communicate Information Technology and System Integration with Agile Development.

Target Market(s)

Our target market is the Federal Government and System Integators in the Washington DC area.

Industry/Entity Type

Government

Requirements
Must have
• The powerpoint design must have a professional look.

```html
<!DOCTYPE html>
<html lang="en">
<head>
<meta charset="utf-8">
<title>Vantage Forge – Presentation Template</title>
<link href="https://fonts.googleapis.com/css2?family=Source+Sans+3:wght@300;400;600;700&display=swap" rel="stylesheet">
<style>
:root{
  --stage:#bfbfbf;
  --brand:#1172bd;
  --brand-dark:#0d5fa0;
  --brand-light:#58bcd9;
  --ink:#555;
  --ink-soft:#8a8a8a;
  --bar:#4a4a4a;
  --paper:#fbfbfb;
  --row:#d0d0d0;
}
*{box-sizing:border-box;margin:0;padding:0}
html,body{width:1200px;height:900px;overflow:hidden}
body{background:var(--stage);position:relative;font-family:"Source Sans 3",sans-serif;color:var(--ink)}
.slide{position:absolute;width:358px;height:277px;overflow:hidden;
  background:linear-gradient(160deg,#fff 0%,var(--paper) 45%,#e2e2e2 100%)}
.s1{left:53px;top:168px}.s2{left:420px;top:168px}.s3{left:791px;top:168px}
.s4{left:53px;top:458px}.s5{left:420px;top:458px}.s6{left:791px;top:458px;background:var(--brand)}
.slide-title{position:absolute;left:19px;top:27px;right:18px;font-size:11.5px;font-weight:400;color:var(--brand);
  border-bottom:1px solid #d4d4d4;padding-bottom:1px;letter-spacing:.2px}
.brand{position:absolute;display:flex;align-items:center;gap:4px;font-weight:700;color:var(--brand-dark);white-space:nowrap}
.brand .mark{background:var(--brand-dark);display:block}
.brand.small{left:13px;bottom:12px;font-size:8px}
.brand.small .mark{width:7px;height:7px}
.footer{position:absolute;left:0;right:0;bottom:0;height:8px}
.footer .line{position:absolute;left:0;right:0;bottom:0;height:3px;background:var(--bar)}
.footer .tab{position:absolute;right:0;bottom:0;width:76px;height:7px;background:var(--brand);
  clip-path:polygon(10px 0,100% 0,100% 100%,0 100%);color:#fff;font-size:4px;text-align:right;padding-right:4px;line-height:7px}
/* welcome */
.s1 .brand{left:29px;top:47px;font-size:15px}
.s1 .brand .mark{width:13px;height:13px}
.s1 .rule{position:absolute;left:0;right:0;top:108px;height:3px;background:var(--bar)}
.s1 .rule-tab{position:absolute;right:0;top:102px;width:78px;height:9px;background:var(--brand);clip-path:polygon(9px 0,100% 0,100% 100%,0 100%)}
.s1 .band{position:absolute;left:0;right:0;top:114px;bottom:0;background:var(--brand)}
.s1 .hello{position:absolute;right:28px;top:180px;text-align:right;color:#fff}
.s1 .hello h1{font-size:24px;font-weight:700;line-height:1}
.s1 .hello p{font-size:17px;font-weight:300;line-height:1.1;margin-top:2px}
.s1 .hello small{display:block;font-size:8px;margin-top:8px}
/* agenda */
.agenda{position:absolute;left:48px;top:72px;width:266px;height:146px;background:#fff;border:1px solid #bbb;border-radius:7px;
  box-shadow:0 1px 3px rgba(0,0,0,.35);padding:14px 13px 0 10px;list-style:none}
.agenda li{display:flex;align-items:center;height:19px;margin-bottom:6.3px}
.agenda .num{width:20px;height:19px;background:linear-gradient(#4f7fc9,#2c5ea8);color:#fff;font-size:13px;text-align:center;line-height:19px;border:1px solid #9fb6db}
.agenda .item{flex:1;margin-left:6px;height:17px;background:var(--row);border-radius:3px;font-size:8.5px;line-height:17px;padding-left:9px;color:#555}
/* photos */
.photo{position:absolute;border:2px solid #fff;box-shadow:0 0 2px rgba(0,0,0,.5)}
.photo.team{left:42px;top:62px;width:76px;height:88px;background:linear-gradient(180deg,#dfe6ee 0%,#9aa3ae 55%,#2e3238 100%)}
.copy{position:absolute;font-size:6.4px;line-height:12.8px;color:var(--ink-soft);text-align:justify;font-weight:300}
.s3 .c1{left:129px;top:66px;width:190px}
.s3 .c2{left:41px;top:161px;width:278px}
.s4 .c1{left:168px;top:58px;width:165px}
.s4 .c2{left:168px;top:159px;width:165px}
.pie{position:absolute;left:22px;top:120px}
/* team */
.person{position:absolute;top:75px;width:100px}
.person .photo{position:relative;display:block;width:58px;height:58px;border:3px solid #777;box-shadow:none;
  background:linear-gradient(180deg,#e6e9ee 0%,#b4bac2 45%,#262a30 100%)}
.person h3{font-size:7.8px;color:var(--brand);font-weight:600;margin-top:17px}
.person p{font-size:4.6px;line-height:8.2px;color:#777}
.divider{position:absolute;top:73px;width:1px;height:130px;background:#999}
/* closing */
.s6 .brand{left:116px;top:138px;color:#fff;font-size:15px}
.s6 .brand .mark{background:#fff;width:13px;height:13px}
</style>
</head>
<body>

<section class="slide s1">
  <div class="brand"><span class="mark"></span>VANTAGE FORGE</div>
  <div class="rule-tab"></div>
  <div class="rule"></div>
  <div class="band"></div>
  <div class="hello">
    <h1>WELCOME</h1>
    <p>TO OUR PRESENTATION</p>
    <small>Birmingham, March 25, 2011</small>
  </div>
</section>

<section class="slide s2">
  <h2 class="slide-title">AGENDA</h2>
  <ol class="agenda">
    <li><span class="num">1</span><span class="item">Lorem ipsum dolor sit amet</span></li>
    <li><span class="num">2</span><span class="item">Lorem ipsum dolor sit amet</span></li>
    <li><span class="num">3</span><span class="item">Lorem ipsum dolor sit amet</span></li>
    <li><span class="num">4</span><span class="item">Lorem ipsum dolor sit amet</span></li>
    <li><span class="num">5</span><span class="item">Lorem ipsum dolor sit amet</span></li>
  </ol>
  <div class="brand small"><span class="mark"></span>VANTAGE FORGE</div>
  <div class="footer"><div class="line"></div><div class="tab">2</div></div>
</section>

<section class="slide s3">
  <h2 class="slide-title">PRESENTATION TITLE</h2>
  <div class="photo team" role="img" aria-label="Photo of a smiling business team in an office"></div>
  <p class="copy c1">Lorem ipsum dolor sit amet, consectetur adipisicing elit, sed do eiusmod tempor incididunt ut labore et dolore magna aliqua. Ut enim ad minim veniam, quis nostrud exercitation ullamco laboris nisi ut aliquip ex ea commodo consequat. Duis aute irure dolor in reprehenderit in voluptate velit esse cillum dolore eu fugiat nulla pariatur.</p>
  <p class="copy c2">Lorem ipsum dolor sit amet, consectetur adipisicing elit, sed do eiusmod tempor incididunt ut labore et dolore magna aliqua. Ut enim ad minim veniam, quis nostrud exercitation ullamco laboris nisi ut aliquip ex ea commodo consequat. Duis aute irure dolor in reprehenderit in voluptate velit esse cillum dolore eu fugiat nulla pariatur.</p>
  <div class="brand small"><span class="mark"></span>VANTAGE FORGE</div>
  <div class="footer"><div class="line"></div><div class="tab">2</div></div>
</section>

<section class="slide s4">
  <h2 class="slide-title">PRESENTATION TITLE</h2>
  <svg class="pie" width="124" height="112" viewBox="0 0 124 112">
    <ellipse cx="62" cy="102" rx="58" ry="4" fill="#000" opacity=".12"/>
    <ellipse cx="60" cy="55" rx="60" ry="40" fill="#2e2e2e"/>
    <rect x="0" y="45" width="120" height="10" fill="#2e2e2e"/>
    <path d="M60 45 L60 5 A60 40 0 0 1 85.4 81.3 Z" fill="#4d4d4d"/>
    <path d="M60 45 L85.4 81.3 A60 40 0 0 1 3.6 58.7 Z" fill="#5e5e5e"/>
    <path d="M60 45 L3.6 58.7 A60 40 0 0 1 8 25 Z" fill="#707070"/>
    <path d="M60 45 L8 25 A60 40 0 0 1 34.6 8.8 Z" fill="#0d5fa0"/>
    <path d="M60 45 L34.6 8.8 A60 40 0 0 1 60 5 Z" fill="#58bcd9"/>
  </svg>
  <p class="copy c1">Lorem ipsum dolor sit amet, consectetur adipisicing elit, sed do eiusmod tempor incididunt ut labore et dolore magna aliqua. Ut enim ad minim veniam, quis nostrud exercitation ullamco laboris nisi ut aliquip ex ea commodo consequat. Duis aute irure dolor in reprehenderit in voluptate velit esse cillum dolore eu fugiat nulla pariatur.</p>
  <p class="copy c2">Lorem ipsum dolor sit amet, consectetur adipisicing elit, sed do eiusmod tempor incididunt ut labore et dolore magna aliqua. Ut enim ad minim veniam, quis nostrud exercitation ullamco laboris nisi ut aliquip ex ea commodo consequat. Duis aute irure dolor in reprehenderit in voluptate velit esse cillum dolore eu fugiat nulla</p>
  <div class="brand small"><span class="mark"></span>VANTAGE FORGE</div>
  <div class="footer"><div class="line"></div><div class="tab">2</div></div>
</section>

<section class="slide s5">
  <h2 class="slide-title">PRESENTATION TITLE</h2>
  <div class="person" style="left:33px">
    <span class="photo" role="img" aria-label="Portrait of a businessman in a dark suit"></span>
    <h3>Martin Hale</h3>
    <p>President &amp; CEO Northgate Oil<br>Director, Ridgeline Energy<br>CEO, Pulse Energy<br>13 years in the deregulated market<br>Graduate of State Law and Tech</p>
  </div>
  <div class="divider" style="left:125px"></div>
  <div class="person" style="left:138px">
    <span class="photo" role="img" aria-label="Portrait of a businessman in a dark suit"></span>
    <h3>Derek Lowe</h3>
    <p>COO Northgate Oil<br>Director, Ridgeline Energy<br>CEO, Pulse Energy<br>13 years in the deregulated market<br>Graduate of State Law and Tech</p>
  </div>
  <div class="divider" style="left:235px"></div>
  <div class="person" style="left:249px">
    <span class="photo" role="img" aria-label="Portrait of a businessman in a dark suit"></span>
    <h3>Paul Brandt</h3>
    <p>VPX Northgate Oil<br>Director, Ridgeline Energy<br>CEO, Pulse Energy<br>13 years in the deregulated market<br>Graduate of State Law and Tech</p>
  </div>
  <div class="brand small"><span class="mark"></span>VANTAGE FORGE</div>
  <div class="footer"><div class="line"></div><div class="tab">2</div></div>
</section>

<section class="slide s6">
  <div class="brand"><span class="mark"></span>VANTAGE FORGE</div>
</section>

</body>
</html>
```